Flyer-Design für Wechseljahresberatung
Zielgruppe
Zielgruppe: überwiegend Frauen
psycholog. Beratung in allen Lebenslagen, Wechseljahresberatung , Gesundheits- und Ernährungsberatung, Fastenbegleitung, Trauerbegleitung, Bachblütenberatung,Klangmassagen
Aufgabenstellung
es geht um einen 6teiligen Kurs für Frauen zwischen Ende 30 bis Ende 60. Beginn der Wechseljahre , Leben in den Wechseljahren und was kommt danach? Wie erkennt man (Frau) körperl. oder seelische Probleme, die schon auf We.jahre hindeuten? Wie gehe Frau damit um? Was passiert in den We.jahren? Was kann Frau selbst tun, um die We.jahre so gut wie möglich zu erleben? Im Kurs werden natürliche Hilfsmittel besprochen und erklärt, Entspannungstechniken vermittelt , die Psyche gestärkt, sodaß die betroffenen Frauen bei auftretenden We.jahrsproblemen die Möglichkeit haben,sich selbst helfen zu können.

```html
<!DOCTYPE html>
<html lang="de">
<head>
<meta charset="utf-8">
<title>Lunavia – Beratung in allen Lebenslagen</title>
<link rel="stylesheet" href="https://fonts.googleapis.com/css2?family=Alfa+Slab+One&family=Tinos:wght@400;700&family=Caveat:wght@500&display=swap">
<style>
  :root {
    --canvas: #ffffff;
    --paper: #e9e9e9;
    --fold: #cfcfcf;
    --card: #ffffff;
    --rose: #d6325c;
    --ink: #3d6468;
    --teal: #6bbbb9;
    --teal-dark: #3f6a6d;
    --white: #ffffff;
  }
  * { box-sizing: border-box; margin: 0; padding: 0; }
  html, body { width: 1131px; height: 1200px; overflow: hidden; background: var(--canvas); }
  .flyer { position: relative; width: 1131px; height: 1200px; font-family: "Tinos", serif; color: var(--ink); }
  .page { position: absolute; top: 30px; height: 1130px; background: var(--paper); overflow: hidden; }
  .page--left { left: 36px; width: 533px; }
  .page--right { left: 572px; width: 532px; }
  .fold { position: absolute; left: 569px; top: 30px; width: 3px; height: 1130px; background: var(--fold); }
  .card { position: absolute; top: 35px; width: 465px; height: 1067px; background: var(--card); border-radius: 24px; overflow: hidden; }
  .page--left .card { left: 34px; }
  .page--right .card { left: 31px; }
  .card__footer { position: absolute; left: 0; right: 0; bottom: 0; height: 282px; background: var(--teal); color: var(--white); text-align: center; }

  .headline { position: absolute; left: 52px; top: 78px; }
  .headline__main { font-family: "Alfa Slab One", serif; font-size: 46px; color: var(--rose); letter-spacing: 1px; line-height: 1; font-weight: 400; }
  .headline__sub { font-family: "Alfa Slab One", serif; font-size: 21px; color: var(--ink); letter-spacing: 0.6px; margin-top: 4px; font-weight: 400; }

  .services { position: absolute; left: 50px; top: 148px; list-style: none; font-size: 25px; line-height: 34px; }
  .services li { position: relative; padding-left: 36px; }
  .services li.cont { padding-left: 36px; }
  .services svg { position: absolute; left: 0; top: 7px; width: 26px; height: 22px; }

  .divider { position: absolute; left: 55px; top: 474px; width: 365px; border-top: 3px dashed var(--ink); }
  .quote { position: absolute; left: 57px; top: 498px; font-size: 25px; line-height: 32px; }
  .intro { position: absolute; left: 57px; top: 578px; width: 370px; font-size: 17.5px; line-height: 29.5px; }

  .schedule__title { font-size: 27px; margin-top: 12px; letter-spacing: 0.5px; }
  .schedule__rows { font-size: 14px; line-height: 27px; color: var(--teal-dark); margin-top: 2px; }
  .prices { width: 290px; margin: 0 auto; font-size: 13.5px; line-height: 27px; color: var(--teal-dark); }
  .prices div { display: flex; justify-content: space-between; }

  .photo { position: absolute; left: 0; top: 0; width: 532px; height: 560px; }
  .badge { position: absolute; left: 51px; top: 361px; width: 152px; height: 152px; border-radius: 50%; background: var(--teal); border: 7px solid var(--white); display: flex; align-items: center; justify-content: center; text-align: center; font-family: "Caveat", cursive; font-size: 30px; line-height: 30px; color: var(--white); }

  .cta { position: absolute; left: 0; width: 465px; top: 520px; text-align: center; font-family: "Caveat", cursive; font-size: 54px; line-height: 68px; color: var(--teal); font-weight: 500; }
  .contact-intro { position: absolute; left: 67px; top: 662px; width: 375px; font-size: 17.5px; line-height: 29.5px; }

  .brand { font-size: 24px; font-weight: 700; color: var(--teal-dark); margin-top: 22px; letter-spacing: 0.5px; }
  .contact { font-size: 21px; line-height: 29px; margin-top: 20px; }
</style>
</head>
<body>
<main class="flyer">
  <section class="page page--left">
    <div class="card">
      <header class="headline">
        <h1 class="headline__main">BERATUNG</h1>
        <p class="headline__sub">IN ALLEN LEBENSLAGEN:</p>
      </header>
      <ul class="services">
        <li><svg viewBox="0 0 26 22"><path d="M2 11 L10 19 L24 3" fill="none" stroke="#d6325c" stroke-width="4" stroke-linecap="round" stroke-linejoin="round"/></svg>Wechseljahresberatung ,</li>
        <li><svg viewBox="0 0 26 22"><path d="M2 11 L10 19 L24 3" fill="none" stroke="#d6325c" stroke-width="4" stroke-linecap="round" stroke-linejoin="round"/></svg>Gesundheits- und</li>
        <li class="cont">Ernährungsberatung,</li>
        <li><svg viewBox="0 0 26 22"><path d="M2 11 L10 19 L24 3" fill="none" stroke="#d6325c" stroke-width="4" stroke-linecap="round" stroke-linejoin="round"/></svg>Fastenbegleitung,</li>
        <li><svg viewBox="0 0 26 22"><path d="M2 11 L10 19 L24 3" fill="none" stroke="#d6325c" stroke-width="4" stroke-linecap="round" stroke-linejoin="round"/></svg>Trauerbegleitung,</li>
        <li><svg viewBox="0 0 26 22"><path d="M2 11 L10 19 L24 3" fill="none" stroke="#d6325c" stroke-width="4" stroke-linecap="round" stroke-linejoin="round"/></svg>Bachblütenberatung,</li>
        <li><svg viewBox="0 0 26 22"><path d="M2 11 L10 19 L24 3" fill="none" stroke="#d6325c" stroke-width="4" stroke-linecap="round" stroke-linejoin="round"/></svg>Klangmassagen</li>
      </ul>
      <div class="divider"></div>
      <p class="quote">Alles hat nur die Bedeutung,<br>die man ihm gibt.</p>
      <p class="intro">Ersperrum dolorro blaceat ureprat uritatqui veliquamet ipicid moluptiam ipic tecture nihilig endandes mo vo-lupici testiae solut mo volor sin cum quam inveniditas autemquae ipsaper feribusdae posto eturit, quam haruptat ommolorpor</p>
      <footer class="card__footer schedule">
        <h2 class="schedule__title">Kurs-Termine:</h2>
        <div class="schedule__rows">
          xxxxxxxxxxx xxxxxxxxxxx<br>xxxxxxxxxxx xxxxxxxxxxx<br>xxxxxxxxxxx xxxxxxxxxxx
        </div>
        <h2 class="schedule__title" style="margin-top:6px">Kurs-Preise:</h2>
        <div class="prices">
          <div><span>xxxxxxxxxxx:</span><span>xx€</span></div>
          <div><span>xxxxxxxxxxx:</span><span>xx€</span></div>
          <div><span>xxxxxxxxxxx:</span><span>xx€</span></div>
        </div>
      </footer>
    </div>
  </section>

  <div class="fold"></div>

  <section class="page page--right">
    <div class="card">
      <p class="cta">Sie sind<br>Interessiert?</p>
      <p class="contact-intro">Kontaktieren Sie uns gerne!&nbsp; blaceat ureprat uritatqui veliquamet ipicid moluptiam ipic tecture nihilig endandes mo volupici testiae solut mo</p>
      <footer class="card__footer">
        <p class="brand">Lunavia</p>
        <p class="contact">Helga Brandt-Wessel<br>Telefon: 0241/60 27 41 53<br>oder&nbsp; +31 (0) 45/7 12 3 84<br>Mail: mondhalm.Beratungspraxis<br>@postfach-mail.de</p>
      </footer>
    </div>
    <svg class="photo" viewBox="0 0 532 560" role="img" aria-label="Foto: rote und rosa Tulpen im Frühlingsbeet">
      <defs>
        <radialGradient id="tulipTones" cx="0.7" cy="0.35" r="0.75">
          <stop offset="0" stop-color="#e84a4f"/>
          <stop offset="0.35" stop-color="#e5659a"/>
          <stop offset="0.7" stop-color="#d96aa0"/>
          <stop offset="1" stop-color="#6aa34a"/>
        </radialGradient>
      </defs>
      <circle cx="303" cy="242" r="238" fill="#ffffff"/>
      <circle cx="303" cy="242" r="229" fill="url(#tulipTones)"/>
    </svg>
    <div class="badge">Fragen<br>kostet<br>nichts!</div>
  </section>
</main>
</body>
</html>
```